Motivationskarten für Trainer und Coach
Zielgruppe
Ich bin Trainer und Coach mit Schwerpunkt Effizienz/ Zeit- und Selbstmanagement sowie Büroorganisation. Meine Kunden buchen bei mir Seminare, um Ihren Arbeitsalltag effizienter zu gestalten und zu strukturieren und Ihre Büroabläufe sowie Prozesse zu optimieren.
Ich möchte gerne 3 verschiedene Postkarten mit Sprüchen von mir gestalten. Postkarten, die man auch verschicken kann und aus denen natürlich meine Kontaktdaten hervorgehen. Mein Logo sollte irgendwo auf der beschreibbaren Seite sichtbar sein. Vorne drauf nur der Spruch und vielleicht eine Zeichnung, eine Karikatur, eine Comiczeichnung oder ein Bild (ich bin offen für alles).
Die Sprüche lauten:
Lieber unperfekt anfangen als gar nicht!
Mach Dir hin und wieder bewusst, wie großartig Du bist!
Frage Dich immer: 'Was ist das Schlimmste, was passieren könnte?' - Es ist selten ein Weltuntergang.
Es sollen drei verschiedene Karten sein, die aber irgendwie zusammenpassen vom Design her.
Meine Hauptzielgruppe, für die auch diese Postkarten hier gedacht sind, sind vor allem Frauen - entweder Frauen, die als Assistentin arbeiten oder selbständig sind.
Aufgabenstellung
Es darf gerne etwas weiblich sein, sollte aber nicht zu bunt und schnörkelig sein. Es darf gerne auffallen. Achtung: Mein Logo sollte ohne Untertitel verwendet werden. Also nur 'Meike Varlow' - ohne 'Training & Coaching'.

```html
<!DOCTYPE html>
<html lang="de">
<head>
<meta charset="utf-8">
<title>Motivationskarte – Großartig</title>
<link rel="stylesheet" href="https://fonts.googleapis.com/css2?family=Leckerli+One&family=Amatic+SC:wght@700&display=swap">
<style>
  :root {
    --paper: #ffffff;
    --sky-light: #7fd3e2;
    --sky: #3ec3d8;
    --sky-deep: #22b6d0;
    --skin-light: #f0c7b4;
    --skin: #e3a995;
    --frame: #d48e97;
    --frame-shadow: rgba(40, 70, 90, 0.35);
    --panel: #f6e9ea;
    --dots: #5a4a4c;
    --band: #cd5166;
    --ink: #111111;
    --white: #ffffff;
  }
  html, body {
    margin: 0;
    padding: 0;
    width: 1200px;
    height: 851px;
    overflow: hidden;
    background: var(--paper);
  }
  .card {
    position: relative;
    width: 1200px;
    height: 851px;
    background: var(--paper);
  }
  .card-front {
    position: absolute;
    left: 40px;
    top: 40px;
    width: 1120px;
    height: 771px;
    overflow: hidden;
    background: radial-gradient(ellipse at 45% 45%, var(--sky-light) 0%, var(--sky) 55%, var(--sky-deep) 100%);
  }
  .finger-photo {
    position: absolute;
    left: 0;
    top: 90px;
    width: 455px;
    height: 681px;
    border-radius: 120px 140px 0 0;
    background: linear-gradient(180deg, var(--skin-light) 0%, var(--skin) 100%);
  }
  .quote-label {
    position: absolute;
    left: 521px;
    top: 90px;
    width: 570px;
    height: 620px;
  }
  .quote-label svg {
    position: absolute;
    left: 0;
    top: 0;
    overflow: visible;
  }
  .quote-line {
    position: absolute;
    left: 16px;
    width: 523px;
    margin: 0;
    text-align: center;
    font-family: "Leckerli One", cursive;
    color: var(--ink);
    white-space: nowrap;
    line-height: 1;
  }
  .quote-main { font-size: 50px; }
  .line-1 { top: 66px; }
  .line-2 { top: 139px; }
  .line-3 { top: 214px; }
  .line-close { top: 468px; }
  .quote-highlight {
    position: absolute;
    left: 16px;
    top: 287px;
    width: 523px;
    height: 158px;
    margin: 0;
    display: flex;
    align-items: center;
    justify-content: center;
    font-family: "Amatic SC", sans-serif;
    font-weight: 700;
    font-size: 150px;
    line-height: 1;
    letter-spacing: 2px;
    color: var(--white);
  }
  .corner-star {
    position: absolute;
    font-family: Arial, sans-serif;
    font-weight: 700;
    font-size: 34px;
    line-height: 1;
    color: var(--ink);
  }
</style>
</head>
<body>
<main class="card">
  <section class="card-front">
    <div class="finger-photo" role="img" aria-label="Foto: drei Finger mit gezeichneten fröhlichen Gesichtern, die sich umarmen und jubeln, vor türkisem Bokeh-Hintergrund"></div>

    <div class="quote-label">
      <svg width="556" height="603" viewBox="0 0 556 603" aria-hidden="true">
        <path d="M30,0 H526 A30 30 0 0 0 556 30 V573 A30 30 0 0 0 526 603 H30 A30 30 0 0 0 0 573 V30 A30 30 0 0 0 30 0 Z"
              fill="var(--frame)" transform="translate(6,7)" opacity="0.35" style="fill: var(--frame-shadow)"/>
        <path d="M30,0 H526 A30 30 0 0 0 556 30 V573 A30 30 0 0 0 526 603 H30 A30 30 0 0 0 0 573 V30 A30 30 0 0 0 30 0 Z"
              fill="var(--frame)"/>
        <path d="M44,15 H512 A28 28 0 0 0 540 43 V560 A28 28 0 0 0 512 588 H44 A28 28 0 0 0 16 560 V43 A28 28 0 0 0 44 15 Z"
              fill="var(--panel)"/>
        <path d="M47,19 H509 A27 27 0 0 0 536 46 V557 A27 27 0 0 0 509 584 H47 A27 27 0 0 0 20 557 V46 A27 27 0 0 0 47 19 Z"
              fill="none" stroke="var(--dots)" stroke-width="1.6" stroke-dasharray="1.6 2.4"/>
        <rect x="16" y="287" width="524" height="158" fill="var(--band)"/>
      </svg>

      <p class="quote-line quote-main line-1">Mach Dir hin und</p>
      <p class="quote-line quote-main line-2">wieder bewusst,</p>
      <p class="quote-line quote-main line-3">wie</p>
      <p class="quote-highlight">GROSSARTIG</p>
      <p class="quote-line quote-main line-close">Du bist!</p>

      <span class="corner-star" style="left:-12px; top:-8px;">*</span>
      <span class="corner-star" style="left:545px; top:-8px;">*</span>
      <span class="corner-star" style="left:-9px; top:577px;">*</span>
      <span class="corner-star" style="left:547px; top:577px;">*</span>
    </div>
  </section>
</main>
</body>
</html>
```